Classic and neutral book cover design

We are looking for a classic and neutral book cover design to be used as the template for a series of books to be published. We are hence looking for a template that will allow us to easily change the title name for all books in this series.
The use of very few colours (black and white is welcome) and few design elements is a big bonus. As a source of inspiration we would like to ask you to view the very simple and
If you think you have a cool idea that can add a twist to the formal classic look don't hesitate. Go for it !
Work will be done for a 30 year old Sweden based cultural non-profit called VĂ©lra (www.velrafoundation.example). We work with the publishing and supporting of post-modern art and literature addressing contemporary topics but are also involved in assisting projects of cultural preservation.
Target Market(s)
The audience is expected to have some form of interest in culture but could range from hobbyist readers to tenure track scholars
Industry/Entity Type
Non-Profit
Requirements
Must have
- General:
- Classic and neutral feel
- Preferably very simple and few shapes
- usage of few colours (black and white is welcome)
Information to be displayed on the cover is:
- Author
- Title
- type of work e.g. play/novel (optional)
- publishing house (in this case "Velra Publishing")
Nice to have
- ideas to prevent it from become boring are of course welcome
Should not have
- - too many colours

```html
<!DOCTYPE html>
<html lang="en">
<head>
<meta charset="utf-8">
<title>Book Cover Template – Velra Publishing</title>
<link rel="stylesheet" href="https://fonts.googleapis.com/css2?family=Gilda+Display&display=swap">
<style>
  :root {
    --cover-black: #000000;
    --cover-white: #ffffff;
    --stone-light: #d9d9d9;
    --stone-mid: #9a9a9a;
    --stone-dark: #5e5e5e;
  }
  html, body {
    margin: 0;
    padding: 0;
    width: 950px;
    height: 1200px;
    overflow: hidden;
    background: var(--cover-black);
  }
  .book-cover {
    position: relative;
    width: 950px;
    height: 1200px;
    background: var(--cover-black);
    color: var(--cover-white);
    font-family: "Gilda Display", "Times New Roman", serif;
    overflow: hidden;
  }
  .cover-title {
    position: absolute;
    top: 160px;
    right: 32px;
    margin: 0;
    font-size: 92px;
    font-weight: 400;
    line-height: 1;
    white-space: nowrap;
    letter-spacing: -0.5px;
  }
  .cover-author {
    position: absolute;
    top: 280px;
    right: 25px;
    margin: 0;
    font-size: 31px;
    line-height: 1;
    white-space: nowrap;
  }
  .cover-publisher {
    position: absolute;
    top: 332px;
    right: 25px;
    margin: 0;
    font-size: 24px;
    line-height: 1;
    white-space: nowrap;
  }
  .column-artwork {
    position: absolute;
    left: 0;
    top: 278px;
    width: 255px;
    height: 922px;
  }
</style>
</head>
<body>
  <main class="book-cover">
    <h1 class="cover-title">Title Would Go Here</h1>
    <p class="cover-author">By John Doe</p>
    <p class="cover-publisher">Velra Publishing</p>

    <svg class="column-artwork" viewBox="0 0 255 922" role="img"
         aria-label="Classical fluted column illustration with grey marble texture">
      <defs>
        <linearGradient id="stoneTone" x1="0" y1="0" x2="1" y2="1">
          <stop offset="0" stop-color="var(--stone-light)"/>
          <stop offset="0.5" stop-color="var(--stone-mid)"/>
          <stop offset="1" stop-color="var(--stone-dark)"/>
        </linearGradient>
      </defs>
      <rect x="0" y="0" width="255" height="922" fill="url(#stoneTone)"/>
    </svg>
  </main>
</body>
</html>
```